Re design and optimization of a website for pension Ora Vahi, a b&b in Tahiti, French Polynesia.

We have a website already : www.pensionoravahi.example

The general idea is to create a new site that is colorful, young and with an exotic, tropical feel since we are on a beautiful island.

The website will be in three languages, all the text is already available on our website, nothing changes.

All pages must have the name of the website (pension ora vahi b&b) our address, mail and phone number
It would be nice to have a link to our mail from every page

Sections have to be easy to update : text and pics

The sections needed are :

- Home page (accueil)

- Prices (tarifs)

- Bookings (reservations) = link to our mailbox : pensionoravahi@post.example )

- Pictures : in three separate categories that will pop up on this page : 1/ pics of the b&b 2/ pics of the surroundings 3/ customer's pics (we'll give new pics, not the current ones)

- Map of Tahiti : we'd like one map that we'll give you and also a Google map with our location, date and local time would be great

- Links (liens)

We let you see what would look best for the top banner and the switches, matching the logo and the pictures, make it nice and tropical !!
We have a few layouts that we did, maybe you will have a better idea of what we want by looking at them, if you can use them and have a good overall feel

We'd like to remind you guys that Tahiti is a dream destination, so you have to come up with something that the visitors will go : wow !!

We cater for backpackers to mid range accommodations and families, it all about a relaxed friendly atmosphere here !

NOTE THAT WE DON'T KNOW MUCH ABOUT PROGRAMMING AND CODING SO IT AS TO BE READY TO GO ON-LINE, ALL YOUR HELP IS APPRECIATED !!!
Also in Tahiti, the
INTERNET is quite low bandwidth so optimization is a must !

P.S : Live demo of the homepage is welcome ;)

We are available to all you for extra infos, good luck

regards,

remy & Pension Ora Vahi

Target Market(s)

Families and couples : individual rooms

Backpackers : Dormitories

people looking for an authentic stay in a familial environment

Customers of all ages and all nationalities

Requirements
Must have
• You must insist on the main page about :
the easy beach access
the breakfast included (with French baguette !)
Airport pick up 24/7
Many activities departing from our place : scuba diving, canyoning, 4x4 tour, rental cars, surf school, para-glide....

Please find a great way to highlight these !

```html
<!DOCTYPE html>
<html lang="en">
<head>
<meta charset="utf-8">
<title>Pension Ora Vahi – Bed &amp; Breakfast, Tahiti</title>
<link href="https://fonts.googleapis.com/css2?family=PT+Sans:wght@400;700&display=swap" rel="stylesheet">
<style>
:root{
  --yellow:#f8f400;
  --nav:#e2561a;
  --green:#6f8f28;
  --blue:#2f6fb4;
  --link:#3b7cc8;
  --text:#4a4a4a;
  --panel:rgba(255,255,255,.82);
  --sea:#3fa7d8;
  --sky:#8fc6ee;
  --sand:#d9c7a6;
}
*{margin:0;padding:0;box-sizing:border-box}
html,body{width:805px;height:1200px;overflow:hidden}
body{
  font-family:"PT Sans",Arial,sans-serif;color:var(--text);position:relative;
  background:linear-gradient(180deg,#5aa3e6 0%,var(--sky) 30%,#bfe3f3 45%,var(--sea) 60%,#6fb9c9 72%,var(--sand) 85%,#b8a78a 100%);
}
.backdrop{position:absolute;inset:0}
.page{position:absolute;left:87px;top:30px;width:634px;height:1150px;box-shadow:0 0 6px rgba(0,0,0,.25)}
.header{position:absolute;left:0;top:0;width:634px;height:112px;background:var(--yellow)}
.phone{position:absolute;right:176px;top:34px;font-weight:700;font-size:17px;color:#111;letter-spacing:.4px;white-space:nowrap}
.phone small{position:absolute;right:0;top:-13px;font-size:9px;font-weight:700}
.brand{position:absolute;left:476px;top:36px;display:flex;align-items:center;gap:6px}
.brand .dot{width:16px;height:16px;border-radius:50%;background:var(--nav);flex:none}
.brand span{font-size:15px;font-weight:700;color:var(--nav);white-space:nowrap}
.nav{position:absolute;left:0;top:98px;width:100%}
.nav a{font-size:9px;font-weight:700;color:var(--nav);text-decoration:none;text-transform:uppercase;position:absolute;white-space:nowrap}
.hero{position:absolute;left:0;top:112px;width:634px;height:287px;
  background:
    radial-gradient(ellipse 120px 90px at 12% 35%,rgba(200,200,195,.55),transparent 70%),
    radial-gradient(ellipse 200px 110px at 55% 80%,rgba(235,235,230,.35),transparent 70%),
    radial-gradient(ellipse 160px 120px at 80% 20%,rgba(70,120,50,.7),transparent 70%),
    linear-gradient(180deg,#5f7a4c 0%,#4c5e40 35%,#55524a 65%,#34322d 100%)}
.content{position:absolute;left:0;top:399px;width:634px;height:701px;background:var(--panel)}
.footer{position:absolute;left:0;top:1100px;width:634px;height:50px;background:var(--yellow)}
.abs{position:absolute}
h2{font-size:17px;font-weight:400;color:var(--green);text-transform:uppercase;letter-spacing:.3px}
h3{font-size:12px;font-weight:700;color:var(--blue)}
p,li{font-size:9px;line-height:1.3}
.photo{position:absolute;border:1px solid #ccc}
.photo.garden{background:linear-gradient(160deg,#4d6b2f,#8a6e3c 60%,#b39a5a)}
.photo.family{background:linear-gradient(180deg,#9fd2ee 0%,#cfe6f2 50%,#e3cfa9 100%);border:4px solid #fff;box-shadow:0 0 3px rgba(0,0,0,.3)}
.photo.kitchen{background:linear-gradient(160deg,#9b5a2c,#c48a52 60%,#6b3d1f)}
.photo.terrace{background:linear-gradient(160deg,#6b5a48,#b7a98f 50%,#5d7c3a)}
.photo.bedroom{background:linear-gradient(160deg,#8a5a36,#d9cdb7 55%,#7a4a2a)}
.features{list-style:none}
.features li{height:19.6px}
.lang{position:absolute;left:440px;top:12px;width:106px;height:18px;border:1px solid #bbb;background:#fff;font-size:8px;padding:3px 6px;color:#555}
.lang::after{content:"▼";position:absolute;right:4px;top:3px;font-size:7px;color:#888}
.card{position:absolute;left:446px;top:71px;width:180px;height:73px}
.card .mark{position:absolute;left:0;top:0;width:18px;height:18px;border-radius:50%;background:#d0d0d0}
.card strong{position:absolute;left:22px;top:4px;font-size:13px;color:#222}
.card p{position:absolute;left:22px;top:22px;font-size:8px;line-height:1.35;color:#222;font-weight:700}
.icon{position:absolute;left:440px;width:50px;height:40px;border-radius:20px}
.act-label{position:absolute;left:501px;font-size:10px;font-weight:700;color:var(--link)}
.social{position:absolute;top:13px;width:21px;height:21px;border-radius:5px}
.footer p{position:absolute;top:21px;font-size:8px;color:#333}
.footer a{font-size:8px;color:#333}
</style>
</head>
<body>
<div class="backdrop" role="img" aria-label="Tropical beach with palm trees, blue sky and turquoise sea"></div>

<div class="page">
  <header class="header">
    <div class="phone"><small>tahiti</small>Tel: 40 12 34</div>
    <div class="brand"><div class="dot"></div><span>Pension Ora Vahi</span></div>
    <nav class="nav">
      <a style="left:7px">Home</a>
      <a style="left:47px">Prices</a>
      <a style="left:91px">Booking</a>
      <a style="left:144px">Gallery</a>
      <a style="left:197px">Map of Tahiti</a>
      <a style="left:276px">Links</a>
    </nav>
  </header>

  <div class="hero" role="img" aria-label="Polynesian dancers in white and black costumes performing at a stone marae among tropical greenery"></div>

  <main class="content">
    <h2 class="abs" style="left:16px;top:14px">Bed &amp; Breakfast</h2>
    <p class="abs" style="left:16px;top:38px">Breakfast with French Baguette is included every morning at the terrace in the garden.</p>
    <p class="abs" style="left:16px;top:58px">Self-service between 7:30 to 10:30 with a fantastic view of the mountain.</p>

    <div class="photo garden" style="left:16px;top:77px;width:160px;height:160px" role="img" aria-label="Garden with tropical flowers"></div>
    <div class="photo family" style="left:196px;top:77px;width:160px;height:160px" role="img" aria-label="Family building a sandcastle on the beach"></div>

    <h3 class="abs" style="left:16px;top:248px">LA PENSION ORA VAHI consists of 3 houses with :</h3>
    <ul class="features abs" style="left:16px;top:267px">
      <li>- 1 Reception (tel - fax - internet)</li>
      <li>- 5 rooms (individual or familial rooms)</li>
      <li>- 2 dorms(4 beds in each)</li>
      <li>- cooking facilities (gas stoves, fridges, micro-waves, plates and cutlery)</li>
      <li>- communal bathrooms</li>
      <li>- television and library</li>
      <li>- many terraces - large gardens (hammocks, lounging area)</li>
      <li>- easy beach access (at 200 meters away)</li>
      <li>Free luggage storage : upon the condition that you return to stay another night.</li>
    </ul>

    <h3 class="abs" style="left:16px;top:444px">Gallery:</h3>
    <div class="photo kitchen" style="left:16px;top:464px;width:117px;height:116px" role="img" aria-label="Shared kitchen"></div>
    <div class="photo terrace" style="left:135px;top:464px;width:118px;height:116px" role="img" aria-label="Terrace with guests at table"></div>
    <div class="photo bedroom" style="left:255px;top:464px;width:117px;height:116px" role="img" aria-label="Bedroom with mosquito net"></div>

    <h3 class="abs" style="left:16px;top:591px;font-weight:400">Other Amenities:</h3>
    <p class="abs" style="left:16px;top:609px;width:400px">With in promixity of Pension Ora Vahi are restaurant - snack - bar, picnic area, kids play area and beach areas that are ideal for snorkeling.</p>

    <div class="lang">Select Language</div>
    <h2 class="abs" style="left:440px;top:43px">Information</h2>
    <div class="card">
      <div class="mark"></div>
      <strong>Pension Ora Vahi</strong>
      <p>BP 000123 Punaauia 98717<br>Moana Nui Tahiti French Polynesia<br>Telephone: 40 12 34 87 00 00</p>
    </div>
    <p class="abs" style="left:440px;top:149px;width:180px">is located in the Paea district - 18.6 kms from Papeete - mountain side.</p>

    <div class="icon" style="top:184px;background:#f0e6b0" role="img" aria-label="Airport pickup plane icon"></div>
    <div class="act-label" style="top:186px">Airport Pickup 24/7</div>
    <p class="abs" style="left:501px;top:201px;width:110px">Etiam pharetra, tellus sit amet congue vulputate.</p>

    <h2 class="abs" style="left:440px;top:237px">Activities</h2>
    <p class="abs" style="left:440px;top:261px;width:185px">Public beach with amenities only 200 meters away ("Vai Nui Park") also featuring activities departing from Pension Ora Vahi:</p>

    <div class="icon" style="top:328px;background:#f2c04a" role="img" aria-label="Scuba mask and snorkel icon"></div>
    <div class="act-label" style="top:329px">Scuba</div>
    <div class="icon" style="top:400px;background:#d6d6d6" role="img" aria-label="Surfer icon"></div>
    <div class="act-label" style="top:406px">Surf School</div>
    <div class="icon" style="top:456px;background:#c96bb8" role="img" aria-label="Paraglider wing icon"></div>
    <div class="act-label" style="top:463px">Paragliding</div>
    <div class="icon" style="top:515px;background:#4a6fc0" role="img" aria-label="Rental car icon"></div>
    <div class="act-label" style="top:521px">Car Rentals</div>
    <div class="icon" style="top:574px;background:#e4e4e4" role="img" aria-label="Sailboat icon"></div>
    <div class="act-label" style="top:578px">Canyoning</div>

    <p class="abs" style="left:440px;top:650px"><strong>Contact Us:</strong> <a style="color:var(--link)">pensionoravahi@post.example</a></p>
  </main>

  <footer class="footer">
    <div class="social" style="left:13px;background:#f28c28" role="img" aria-label="News feed"></div>
    <div class="social" style="left:37px;background:#3f63ad" role="img" aria-label="Social page"></div>
    <div class="social" style="left:61px;background:#4ab0e3" role="img" aria-label="Social feed"></div>
    <p style="left:204px">Copyright © 2011. All Rights Reserved.</p>
    <p style="left:463px"><a>About Us</a> &nbsp; <a>Contact Us</a> &nbsp; <a>Terms Of Service</a></p>
  </footer>
</div>
</body>
</html>
```